New Alcoholic Spiked Seltzer Line

We need a can design for a line of low calorie alcoholic seltzer. This product is a sparkling water and vodka drink with no sugar added in a slim 12 oz can.

This is a lighter, healthier, alternative to the sugary ready-to-drinks on the market. The product contains only 3 ingredients: Vodka, Water and Natural Flavors. It has only 100 calories but still has 5% alcohol, so you don't need to sacrifice alcohol to cut calories.

This product also does not contain any preservatives.

We want this design to communicate the following objectives to the consumer and in this order:

1. Appetizing product
2.Low calorie
3.Communicate the type of beverage (Spiked Seltzer)

The brand name of the product is VELKA.

The flavor of the product needed to be used for the design is Mango-Orange.

Comparable products are:

www.brisavelfizz.example/
https://www.tarnowbubble.example
https://quellrind.example/

The designs should not infringe or copy the creative directions of the products mentionned above. They are only given so that you can better understand the type of product we are developing.

Target Market(s)

Young Professional women between the ages of 25 and 44

Industry/Entity Type

Product

Colors

Designer to choose colors to be used in the design.

Requirements
Must have
• Design extendibility, meaning it can be adapted for other flavors.
• This is a new category in the market we are targeting, so consumers must easily be able to identify what type of product this is.

```html
<!DOCTYPE html>
<html lang="en">
<head>
<meta charset="utf-8">
<title>VELKA Spiked Seltzer – Mango Can Label</title>
<link rel="stylesheet" href="https://fonts.googleapis.com/css2?family=Montserrat:wght@800;900&family=Marcellus+SC&display=swap">
<style>
  :root {
    --page: #ffffff;
    --label-light: #fbfbfb;
    --label-shade: #e6e6e7;
    --ink: #111111;
    --orange: #f0921e;
    --orange-deep: #e07d10;
    --lime: #d7f24a;
    --rule: #b9b9bb;
    --mango-light: #f6b13a;
    --mango-dark: #e28a12;
  }
  * { box-sizing: border-box; margin: 0; padding: 0; }
  html, body {
    width: 927px;
    height: 1200px;
    overflow: hidden;
    background: var(--page);
  }
  .canvas {
    position: relative;
    width: 927px;
    height: 1200px;
  }
  .can-label {
    position: absolute;
    left: 287px;
    top: 167px;
    width: 359px;
    height: 867px;
    background: linear-gradient(90deg, var(--label-shade) 0%, var(--label-light) 30%, var(--label-light) 70%, var(--label-shade) 100%);
    color: var(--ink);
  }
  .accent-band {
    position: absolute;
    left: 0;
    width: 100%;
    height: 23px;
    background: linear-gradient(180deg, var(--orange) 0%, var(--orange) 50%, var(--lime) 100%);
  }
  .accent-band--top { top: 0; }
  .accent-band--bottom { top: 844px; }

  .brand {
    position: absolute;
    top: 168px;
    left: 0;
    width: 100%;
    height: 72px;
    display: flex;
    align-items: center;
    justify-content: center;
    gap: 14px;
  }
  .brand__dot {
    width: 40px;
    height: 40px;
    border-radius: 50%;
    background: var(--orange);
    flex: none;
  }
  .brand__name {
    font-family: "Montserrat", sans-serif;
    font-weight: 900;
    font-size: 64px;
    line-height: 1;
    letter-spacing: 1px;
    color: var(--ink);
  }

  .category {
    position: absolute;
    top: 372px;
    left: 0;
    width: 100%;
    text-align: center;
    font-family: "Montserrat", sans-serif;
    font-weight: 800;
    font-size: 54px;
    line-height: 56px;
    letter-spacing: 0;
  }

  .rule {
    position: absolute;
    left: 0;
    width: 100%;
    height: 3px;
    background: var(--rule);
  }
  .rule--upper { top: 500px; }
  .rule--lower { top: 591px; }

  .flavor-band {
    position: absolute;
    top: 513px;
    left: 0;
    width: 100%;
    height: 69px;
    background: linear-gradient(90deg, var(--orange-deep) 0%, var(--orange) 35%, var(--orange) 70%, var(--lime) 100%);
    display: flex;
    align-items: center;
    justify-content: center;
    font-family: "Montserrat", sans-serif;
    font-weight: 800;
    font-size: 48px;
    letter-spacing: 4px;
  }

  .flavor-art {
    position: absolute;
    top: 600px;
    left: 125px;
    width: 160px;
    height: 78px;
  }

  .calorie-claim {
    position: absolute;
    top: 694px;
    left: 0;
    width: 100%;
    text-align: center;
    font-family: "Marcellus SC", serif;
  }
  .calorie-claim__headline {
    font-size: 42px;
    line-height: 32px;
    letter-spacing: 1px;
  }
  .calorie-claim__detail {
    margin-top: 6px;
    font-size: 18px;
    line-height: 20px;
    letter-spacing: 1px;
    text-transform: lowercase;
    font-variant: small-caps;
  }

  .can-facts {
    position: absolute;
    top: 796px;
    left: 18px;
    right: 16px;
    display: flex;
    justify-content: space-between;
    font-family: "Marcellus SC", serif;
    font-size: 20px;
    line-height: 24px;
    letter-spacing: 1px;
  }
</style>
</head>
<body>
<main class="canvas">
  <section class="can-label">
    <div class="accent-band accent-band--top"></div>

    <div class="brand">
      <span class="brand__dot"></span>
      <span class="brand__name">VELKA</span>
    </div>

    <h1 class="category">SPIKED<br>SELTZER</h1>

    <div class="rule rule--upper"></div>
    <div class="flavor-band">MANGO</div>
    <div class="rule rule--lower"></div>

    <svg class="flavor-art" viewBox="0 0 160 78" role="img" aria-label="Illustration of a ripe mango with two green leaves">
      <defs>
        <linearGradient id="mangoTone" x1="0" y1="0" x2="1" y2="1">
          <stop offset="0" stop-color="#f6b13a"/>
          <stop offset="1" stop-color="#e28a12"/>
        </linearGradient>
      </defs>
      <rect x="0" y="0" width="160" height="78" rx="36" fill="url(#mangoTone)"/>
    </svg>

    <div class="calorie-claim">
      <p class="calorie-claim__headline">LOW<br>CALORIE</p>
      <p class="calorie-claim__detail">Only 100 calories</p>
    </div>

    <div class="can-facts">
      <span>12 oz can.</span>
      <span>5% alcohol</span>
    </div>

    <div class="accent-band accent-band--bottom"></div>
  </section>
</main>
</body>
</html>
```